Cleaning Company needs a new business card design

Hi, We are looking for new business card designs to update with our latest logo and company information.
We would like to see designs using the colours:
Royal Blue #4169E1 - this is our company colour so this has to be in there. Please feel free to experiment with other colours.
Must include:
Front of business card:
Logo
Back of the business card:
0800 529 6081
07438 915 702
Email: info@pkrtidyhomes.co.uk
Web: www.pkrtidyhomes.co.uk
Services:
End of Tenancy
Carpet & Upholstery
Regular & One Off
all work fully insured.
The front of the business card with the logo can be made to look raised print. The blue man to be a shiny finish.
The business card needs to be presented in a matt finish
The business must be in the following styles:
Standard Square with rounded corners.
Thank you to all that take part in this.
Target Market(s)
Men and Women of different ages in the UK.
Industry/Entity Type
House Cleaning
Contact Information for Business Card
Front of business card:
Logo
0800 529 6081
07438 915 702
Email: pkrtidy@mailbox-demo.co.uk
Services:
End of Tenancy
Carpet & Upholstery
Regular & One Off
all work fully insured.

```html
<!DOCTYPE html>
<html lang="en">
<head>
<meta charset="utf-8">
<title>PKR Tidy Homes – Business Card</title>
<link href="https://fonts.googleapis.com/css2?family=Oswald:wght@300;500;700&display=swap" rel="stylesheet">
<style>
  :root {
    --royal: #4169e1;
    --blue-light: #74a3d1;
    --blue-mid: #4a84c2;
    --blue-deep: #0d2f66;
    --navy: #14264f;
    --ink: #1b1b1f;
    --grey-light: #f3f3f4;
    --grey-mid: #c9cacd;
    --figure: #c4c5cb;
    --stage: #e8eaee;
    --white: #ffffff;
  }
  * { box-sizing: border-box; margin: 0; padding: 0; }
  html, body {
    width: 1200px; height: 1200px; overflow: hidden;
    background: var(--stage);
    font-family: "Oswald", "Arial Narrow", sans-serif;
  }
  .sheet { position: relative; width: 1200px; height: 1200px; }

  .card {
    position: absolute; left: 170px; width: 860px; height: 520px;
    border-radius: 40px; overflow: hidden;
    box-shadow: 0 14px 30px rgba(0,0,0,0.18);
  }
  .card--front { top: 60px; background: var(--white); }
  .card--back  { top: 620px; background: linear-gradient(100deg, var(--grey-mid) 0%, var(--grey-light) 45%, var(--white) 75%, var(--grey-light) 100%); }

  /* front */
  .front__top {
    position: absolute; left: 0; top: 0; width: 100%; height: 110px;
    background: linear-gradient(90deg, var(--blue-mid), var(--blue-light));
  }
  .front__band {
    position: absolute; left: 0; top: 110px; width: 100%; height: 170px;
    background: var(--white);
    display: flex; align-items: center; justify-content: center; gap: 14px;
  }
  .front__bottom {
    position: absolute; left: 0; top: 280px; width: 100%; height: 240px;
    background: linear-gradient(160deg, var(--blue-mid) 0%, var(--blue-deep) 45%, var(--blue-mid) 100%);
  }
  .brand-dot { width: 22px; height: 22px; border-radius: 50%; background: var(--royal); }
  .brand-name {
    font-weight: 500; font-size: 58px; color: var(--navy);
    letter-spacing: 1px; line-height: 1;
  }

  /* back */
  .back__band {
    position: absolute; left: 0; top: 0; width: 100%; height: 215px;
    background: linear-gradient(90deg, var(--blue-deep) 0%, var(--blue-mid) 35%, var(--blue-mid) 100%);
  }
  .figure {
    position: absolute; z-index: 0;
    background: linear-gradient(180deg, var(--figure), rgba(196,197,203,0.35));
    border-radius: 60px 60px 20px 20px;
  }
  .figure--left  { left: 30px; top: 210px; width: 140px; height: 280px; }
  .figure--right { right: 30px; top: 310px; width: 140px; height: 210px; }

  .back__heading { position: absolute; z-index: 1; left: 230px; top: 40px; }
  .back__title { font-weight: 700; font-size: 52px; color: var(--white); line-height: 1; }
  .back__subtitle {
    font-weight: 300; font-size: 28px; color: #9fc0e6; line-height: 1.1;
    padding-bottom: 6px; border-bottom: 1px solid #9fc0e6; width: 300px;
  }
  .back__claim {
    font-weight: 700; font-size: 36px; color: var(--navy); line-height: 1.1;
    text-transform: uppercase; margin-top: 4px; white-space: nowrap;
  }
  .back__brand {
    position: absolute; z-index: 1; right: 40px; top: 110px; text-align: right;
    font-weight: 500; font-size: 30px; color: var(--white); line-height: 1.1;
  }

  .contact { position: absolute; z-index: 1; left: 230px; top: 245px; list-style: none; }
  .contact li {
    display: flex; align-items: center; gap: 12px;
    font-weight: 500; font-size: 22px; color: var(--ink);
    height: 36px; text-transform: uppercase; white-space: nowrap;
  }
  .contact svg { width: 22px; height: 22px; flex: none; }

  .services { position: absolute; z-index: 1; left: 600px; top: 285px; list-style: none; }
  .services__label {
    font-weight: 500; font-size: 22px; color: var(--royal); margin-bottom: 4px;
    text-transform: uppercase;
  }
  .services li {
    font-weight: 500; font-size: 22px; color: var(--ink); line-height: 1.35;
    text-transform: uppercase; white-space: nowrap;
  }
</style>
</head>
<body>
<main class="sheet">

  <section class="card card--front" aria-label="Business card front">
    <div class="front__top"></div>
    <div class="front__band">
      <span class="brand-dot"></span>
      <span class="brand-name">PKR Tidy Homes Limited</span>
    </div>
    <div class="front__bottom"></div>
  </section>

  <section class="card card--back" aria-label="Business card back">
    <div class="back__band"></div>
    <div class="figure figure--left" role="img" aria-label="Faint grey figure of a person vacuuming"></div>
    <div class="figure figure--right" role="img" aria-label="Faint grey figure of a person vacuuming"></div>

    <div class="back__heading">
      <p class="back__title">PKR</p>
      <p class="back__subtitle">TIDY HOMES</p>
      <p class="back__claim">All work fully insured</p>
    </div>

    <p class="back__brand">PKR Tidy Homes<br>Limited</p>

    <ul class="contact">
      <li>
        <svg viewBox="0 0 24 24" aria-hidden="true"><path fill="#1b1b1f" d="M6.6 10.8a15 15 0 0 0 6.6 6.6l2.2-2.2a1 1 0 0 1 1-.25 11 11 0 0 0 3.6.6 1 1 0 0 1 1 1V20a1 1 0 0 1-1 1A17 17 0 0 1 3 4a1 1 0 0 1 1-1h3.5a1 1 0 0 1 1 1 11 11 0 0 0 .6 3.6 1 1 0 0 1-.25 1z"/></svg>
        0800 529 6081
      </li>
      <li>
        <svg viewBox="0 0 24 24" aria-hidden="true"><rect x="7" y="2" width="10" height="20" rx="2" fill="#1b1b1f"/><rect x="9" y="5" width="6" height="11" fill="#ffffff"/></svg>
        07438 915 702
      </li>
      <li>
        <svg viewBox="0 0 24 24" aria-hidden="true"><rect x="2" y="5" width="20" height="14" rx="1" fill="#1b1b1f"/><path d="M3 6l9 7 9-7" stroke="#ffffff" stroke-width="1.6" fill="none"/></svg>
        pkrtidy@mailbox-demo.co.uk
      </li>
      <li>
        <svg viewBox="0 0 24 24" aria-hidden="true"><circle cx="12" cy="12" r="10" fill="#1b1b1f"/><ellipse cx="12" cy="12" rx="4" ry="10" stroke="#ffffff" stroke-width="1.2" fill="none"/><path d="M2 12h20" stroke="#ffffff" stroke-width="1.2"/></svg>
        www.pkrtidyhomes.co.uk
      </li>
    </ul>

    <ul class="services">
      <li class="services__label">Services:</li>
      <li>-End of Tenancy</li>
      <li>-Carpet &amp; Upholstery</li>
      <li>-Regular &amp; One Off</li>
    </ul>
  </section>

</main>
</body>
</html>
```